Travel Company is looking for a STAND OUT Business Card

I need a unique Business Card that will truly stand out. Nothing too busy. Simple is good, right? Not looking for a standard design either. No cookie cutter layout. We are a Travel Company that works more with Companies than Travelers. I had an idea to focus and emphasis on the 2 logo a bit more. This is not necessary, however thought it would look interesting. I am just looking for something interesting and a bit different. Does't have to completely off the wall crazy, just not your run of the mill business card.

Target Market(s)

Hoteliers, Resort Management, Call Centers, Executives, Travelers, Families, Businesses

Industry/Entity Type

Hospitality

Contact Information for Business Card

President/CEO - Marcus T Bellamy (title not necessary if design doesn't allow for it)
contact - (407) 555-0186
email - mbellamy@wayfarenow.example
address - 4812 Quillmore Ave #164
Orlando, FL 32804
website - www.wayfarenow.example

Font styles to use
Serif
Other font styles liked:
• Avenir Next LT Pro BOLD

Requirements
Must have
• simple look and design. Unique design
Nice to have
• I attached the 2 logo separate from the main logo. This can be used separately from the Main Logo, together with the main logo or as main logo. I included the logo font. Use it or not, designers choice.
Should not have
• cookie cutter design. Little use of red other than the logo

```html
<!DOCTYPE html>
<html lang="en">
<head>
<meta charset="utf-8">
<title>Wayfare Now – Business Card</title>
<link href="https://fonts.googleapis.com/css2?family=Nunito+Sans:wght@400;700;800&display=swap" rel="stylesheet">
<style>
  :root {
    --brand-red: #ec1f27;
    --paper-white: #ffffff;
    --ink-black: #161616;
    --backdrop: #2b2d31;
    --card-radius: 24px;
  }
  html, body {
    margin: 0;
    padding: 0;
    width: 1200px;
    height: 900px;
    overflow: hidden;
    background: var(--backdrop);
    font-family: "Nunito Sans", sans-serif;
  }
  .canvas {
    width: 1200px;
    height: 900px;
    display: flex;
    flex-direction: column;
    align-items: center;
    justify-content: center;
    gap: 70px;
  }
  .card {
    position: relative;
    width: 620px;
    height: 354px;
    border-radius: var(--card-radius);
    overflow: hidden;
    box-shadow: 0 14px 30px rgba(0, 0, 0, 0.35);
  }

  /* Front: contact side */
  .card--front {
    background: var(--paper-white);
  }
  .front-band {
    position: absolute;
    inset: 0;
    background: var(--brand-red);
    clip-path: polygon(0 0, 58% 0, 30% 100%, 0 100%);
  }
  .contact {
    position: absolute;
    left: 36px;
    top: 34px;
    color: var(--paper-white);
  }
  .contact__name {
    margin: 0;
    font-size: 22px;
    font-weight: 800;
    letter-spacing: 0.2px;
  }
  .contact__title {
    margin: 2px 0 26px;
    font-size: 15px;
    font-weight: 400;
  }
  .contact__list {
    margin: 0 0 22px;
    padding: 0;
    list-style: none;
    font-size: 13px;
    line-height: 1.55;
  }
  .contact__address {
    margin: 0;
    font-style: normal;
    font-size: 13px;
    line-height: 1.55;
  }
  .wordmark {
    font-weight: 800;
    letter-spacing: -0.5px;
    line-height: 1;
    white-space: nowrap;
  }
  .card--front .wordmark {
    position: absolute;
    left: 52%;
    top: 50%;
    transform: translateY(-50%);
    font-size: 44px;
    color: var(--ink-black);
  }

  /* Back: brand side */
  .card--back {
    background: var(--brand-red);
    display: flex;
    align-items: center;
    justify-content: center;
  }
  .card--back .wordmark {
    font-size: 58px;
    color: var(--paper-white);
  }
</style>
</head>
<body>
  <main class="canvas">
    <section class="card card--front" aria-label="Business card front">
      <div class="front-band"></div>
      <div class="contact">
        <h1 class="contact__name">Marcus T Bellamy</h1>
        <p class="contact__title">President/CEO</p>
        <ul class="contact__list">
          <li>(407) 555-0186</li>
          <li>mbellamy@wayfarenow.example</li>
          <li>www.wayfarenow.example</li>
        </ul>
        <address class="contact__address">
          4812 Quillmore Ave<br>
          #164 Orlando, FL 32804
        </address>
      </div>
      <div class="wordmark">wayfare now</div>
    </section>

    <section class="card card--back" aria-label="Business card back">
      <div class="wordmark">wayfare now</div>
    </section>
  </main>
</body>
</html>
```